Income Tax and Accounting Brochure

I need a brochure using my new logo (file attached). I do tax work and accounting work. I am an EA (QDX Enrolled Agent - logo attached) and would like this incorporated into the brochure. I also have a MSA in Accounting. Please incorporate the text that I have provided in the brochure.

Target Market(s)

Tax Clients - both business and individuals

Industry/Entity Type

Accounting

Colors
0054AA
0677BA
7BADD7
CADEEF
E8F1F8

Requirements
Must have
• Use my logo and the QDX EA file in the brochure
Nice to have
• I would like to see a brochure that I can customize with my own text if possible.

```html
<!DOCTYPE html>
<html lang="en">
<head>
<meta charset="utf-8">
<title>Northvale Accounting &amp; Consulting – Brochure Front</title>
<link rel="stylesheet" href="https://fonts.googleapis.com/css2?family=Montserrat:wght@300;500;600;700&family=Roboto+Condensed:wght@400&display=swap">
<style>
  :root {
    --brand-blue: #0d4a9a;
    --sky-blue: #2a7fc9;
    --navy: #283593;
    --brand-red: #d8063f;
    --ink: #2a2a2a;
    --paper: #efeeed;
    --white: #ffffff;
    --badge: #8f8a72;
  }
  * { margin: 0; padding: 0; box-sizing: border-box; }
  html, body { width: 876px; height: 1200px; overflow: hidden; background: var(--white); }
  .brochure {
    position: relative;
    width: 876px;
    height: 1200px;
    overflow: hidden;
    background: linear-gradient(180deg, #f2f1f0 0%, #ebe9e8 60%, #e6e3e2 100%);
    font-family: "Roboto Condensed", sans-serif;
    color: var(--ink);
  }
  .backdrop { position: absolute; inset: 0; width: 100%; height: 100%; }

  .brand { position: absolute; left: 58px; top: 48px; display: flex; align-items: center; gap: 12px; }
  .brand-mark { width: 70px; height: 70px; border-radius: 50%; background: var(--brand-blue); }
  .brand-name {
    font-family: "Montserrat", sans-serif; font-weight: 600; color: var(--brand-blue);
    font-size: 21px; line-height: 1.25; letter-spacing: 0.5px;
  }
  .brand-name .sub { display: block; font-size: 17px; letter-spacing: 3px; }
  .brand-url {
    position: absolute; left: 148px; top: 120px;
    font-family: "Montserrat", sans-serif; font-weight: 500;
    font-size: 12.5px; letter-spacing: 1.6px; color: var(--brand-red);
  }
  .credential-badge { position: absolute; left: 152px; top: 154px; width: 200px; height: 48px; background: var(--badge); opacity: .75; }

  .tagline {
    position: absolute; left: 80px; top: 232px;
    font-family: "Montserrat", sans-serif; font-size: 41px; line-height: 40px; color: var(--brand-blue); font-weight: 500;
  }
  .tagline .lead { display: block; color: var(--brand-red); font-weight: 300; }

  .about { position: absolute; right: 73px; top: 800px; text-align: right; }
  .about-title { font-family: "Montserrat", sans-serif; font-weight: 700; font-size: 58px; line-height: 58px; color: var(--sky-blue); }
  .about-name { font-size: 39px; line-height: 40px; color: var(--brand-red); }
  .about-role {
    display: inline-block; margin-top: 2px; padding: 1px 4px 1px 26px;
    background: var(--brand-red); color: var(--white); font-size: 22px; line-height: 26px;
  }

  .copy { position: absolute; font-size: 17px; line-height: 21px; }
  .copy p + p { margin-top: 8px; }
  .copy-services { left: 470px; top: 937px; width: 340px; }
  .copy-credentials { left: 58px; top: 1045px; width: 420px; }
  .highlight-band { position: absolute; left: 0; top: 1047px; width: 221px; height: 19px; background: var(--brand-blue); }
  .highlight { color: var(--white); }
</style>
</head>
<body>
<main class="brochure">
  <svg class="backdrop" viewBox="0 0 1240 1755" preserveAspectRatio="none" aria-hidden="false">
    <defs>
      <linearGradient id="photoTone" x1="0" y1="0" x2="1" y2="1">
        <stop offset="0" stop-color="#f3f1ef"/>
        <stop offset="0.45" stop-color="#d9cfc7"/>
        <stop offset="0.75" stop-color="#6f7683"/>
        <stop offset="1" stop-color="#3b4456"/>
      </linearGradient>
      <linearGradient id="chevronTone" x1="0" y1="0" x2="1" y2="1">
        <stop offset="0" stop-color="#d8063f"/>
        <stop offset="0.35" stop-color="#283593"/>
        <stop offset="0.6" stop-color="#d8063f"/>
        <stop offset="0.8" stop-color="#2a7fc9"/>
        <stop offset="1" stop-color="#0d4a9a"/>
      </linearGradient>
    </defs>
    <polygon role="img" aria-label="Photo of two smiling businessmen in suits reviewing a tablet in a bright office"
             fill="url(#photoTone)" points="0,0 1240,0 1240,230 515,955 0,440"/>
    <polygon class="divider-stripe" fill="#ffffff" points="0,440 515,955 1240,230 1240,268 515,993 0,480"/>
    <polygon role="img" aria-label="Chevron of red and blue geometric triangles"
             fill="url(#chevronTone)" points="0,480 515,993 1240,268 1240,685 413,1510 0,1097"/>
  </svg>

  <div class="brand">
    <span class="brand-mark"></span>
    <span class="brand-name">NORTHVALE ACCOUNTING<span class="sub">&amp; CONSULTING, LLC</span></span>
  </div>
  <div class="brand-url">www.northvaleaccounting.com</div>
  <div class="credential-badge" role="img" aria-label="QDX Enrolled Agent credential badge"></div>

  <h1 class="tagline"><span class="lead">Think..</span>whatever is<br>always right!</h1>

  <section class="about">
    <h2 class="about-title">About</h2>
    <div class="about-name">Marian T Holloway</div>
    <div class="about-role">MSA EA (Principal)</div>
  </section>

  <div class="copy copy-services">
    <p>I provide individual and small business tax services, Accounting, bookkeeping, QDX representation, insurance audit representation, business license assistance and more.</p>
    <p>I have experience working with a wide variety of clients from the point where they first decide they want to start a business. They are often unsure about what to do first- I have a lot of experience to offer you.</p>
  </div>

  <div class="highlight-band"></div>
  <div class="copy copy-credentials">
    <p><span class="highlight">I have a Masters' Degree</span> in accounting and am an QDX Enrolled Agent. I am also a LedgerPro Advanced Certified Consultant in both the online and desktop products including Enterprise and Point of Sale.</p>
  </div>
</main>
</body>
</html>
```